Website Refresh for Brightfield Childcare

Company Overview:

Brightfield Childcare is a trusted provider of early childhood education and care services. We are dedicated to creating a nurturing environment where children can grow, learn, and thrive. Our centres offer a range of programs tailored to different age groups, and we pride ourselves on our commitment to quality, safety, and community engagement.

Project Overview:

We are looking for a talented designer to refresh our existing website (https://brightfieldchildcare.com.au/).

The primary goal is to modernize the design while keeping the content unchanged. The new design should be user-friendly, visually appealing, and reflective of our brand’s values. The website should share a similar "DNA" with our sister company’s website, Oak Harbour Early Learning, (https://oakharbourelc.com.au/) but it should not be a direct copy.

We want a design that mirrors our brand's shared values while introducing unique elements that distinguish Brightfield Childcare.

Design Requirements:
1. Home Page
2. About Us
3. Parent Info
4. Our Programs
5. Template for Centre Pages
6. Contact Us / Enrolment (Optional)

Design Style and Inspiration:
• The design should align with the "DNA" of Oak Harbour Early Learning, but also bring in unique design elements to set Brightfield Childcare apart.
• We are looking for a clean, modern, and professional design that is easy to navigate.
• The colour scheme and design elements should reflect our brand’s identity—welcoming, warm, and child-friendly without being overly childish.
• The design must be responsive, ensuring a great user experience across all devices, including desktops, tablets, and mobile phones.
• Accessibility is crucial—use clear fonts, sufficient contrast, and straightforward navigation.

Content Considerations:
• The content will remain the same; the focus is on enhancing the design and user interface.

Deliverables:
• High-fidelity mock-ups for each of the specified pages.
• Responsive design layouts for desktop, tablet, and mobile views.
• Design files should be delivered in a format compatible with any development team.

Target Audience:
• Parents of young children looking for childcare services.
• Community members interested in learning more about our centres and programs.

Submission Requirements:
• A brief explanation of your design approach and how it aligns with our branding goals.
• A portfolio showcasing your previous work, especially any similar projects.
• All requested deliverables must be included in your submission.

Judging Criteria:
• Alignment with our brand identity and the "DNA" of our sister company’s website.
• Visual appeal and user-friendliness of the design.
• Responsiveness and adaptability across different devices.
• Creativity and uniqueness in differentiating Brightfield Childcare from our sister company.

Notes:
• While we would like to engage the winning artist with the coding / css work, its not mandatory.
• Feel free to ask for any digital assets you need to complete the work.
• Main site to be refreshed - https://brightfieldchildcare.com.au/
• Sister site to take inspiration from - https://oakharbourelc.com.au/

Target Market(s)

A) Parents of young children looking for childcare services. B)Community members interested in learning more about our centres and programs.

Industry/Entity Type

Child Care

Number of Pages Required

5+ page

Requirements
Must have
• Please read description
Nice to have
• Please read description
Should not have
• Please read description

```html
<!DOCTYPE html>
<html lang="en">
<head>
<meta charset="utf-8">
<title>Enrolment | Brightfield Childcare</title>
<link href="https://fonts.googleapis.com/css2?family=Roboto:wght@400;500;700;900&display=swap" rel="stylesheet">
<style>
:root{
  --purple:#86178a;
  --green:#34a12f;
  --green-dark:#2a8c26;
  --orange:#ff7b06;
  --blue:#1b95cf;
  --ink:#111;
  --muted:#666;
  --line:#d6d6d6;
  --footer:#2c2f2a;
  --white:#fff;
}
*{box-sizing:border-box;margin:0;padding:0}
html,body{width:810px;height:1200px;overflow:hidden}
body{position:relative;background:var(--white);font-family:"Roboto",Arial,sans-serif;color:var(--ink)}
.abs{position:absolute}
.backdrop{position:absolute;left:0;top:0}
/* header */
.brand{left:41px;top:14px;font-size:19px;font-weight:700;color:var(--green);display:flex;align-items:center;gap:5px}
.brand .dot{width:12px;height:12px;border-radius:50%;background:var(--green)}
.contact{display:flex;align-items:center;gap:8px;top:12px}
.contact .ic{width:29px;height:29px;border-radius:50%;display:flex;align-items:center;justify-content:center}
.contact strong{display:block;font-size:9px;font-weight:500}
.contact span{display:block;font-size:8px;color:var(--muted);margin-top:3px}
.nav{left:40px;top:52px;width:729px;height:30px;border-radius:15px;background:var(--purple);display:flex;align-items:center}
.nav a{position:absolute;color:var(--white);font-size:9px;font-weight:700;text-decoration:none;letter-spacing:.2px}
.nav .divider{position:absolute;left:580px;top:6px;width:1px;height:18px;background:rgba(255,255,255,.5)}
.nav .search{position:absolute;left:590px;font-size:7.5px;color:var(--white)}
/* hero */
.hero-title{left:0;width:810px;top:128px;text-align:center;color:var(--white);font-size:36px;font-weight:900;letter-spacing:1px}
.hero-copy{left:190px;width:430px;text-align:center;color:var(--white);font-size:7.8px;line-height:13px}
.hero-copy.lead{top:175px;font-weight:500}
.hero-copy.note{top:206px}
/* form card */
.card{left:86px;top:258px;width:638px;height:564px;background:var(--white);border-radius:5px;box-shadow:0 2px 8px rgba(0,0,0,.08)}
.card-title{left:118px;top:274px;font-size:18px;font-weight:700;color:var(--green)}
.card-rule{left:118px;top:305px;width:576px;height:1px;background:var(--green)}
.label{font-size:8px;font-weight:500}
.field{height:24px;border:1px solid var(--line);border-radius:5px;font-size:7.8px;color:var(--muted);padding:0 13px;display:flex;align-items:center}
.field.full{left:116px;width:578px}
.field.left{left:116px;width:287px}
.field.right{left:407px;width:287px;padding-left:11px}
.field .toggle{position:absolute;right:0;top:0;width:31px;height:22px;border-left:1px solid var(--line);display:flex;align-items:center;justify-content:center}
.field.area{align-items:flex-start;padding-top:7px;height:64px}
.submit{left:116px;top:772px;width:70px;height:28px;border-radius:14px;background:var(--orange);color:var(--white);font-size:9px;font-weight:500;display:flex;align-items:center;justify-content:center}
/* footer */
.foot-brand{left:71px;top:1020px;font-size:20px;font-weight:700;color:var(--green);display:flex;align-items:center;gap:5px}
.foot-brand .dot{width:12px;height:12px;border-radius:50%;background:var(--green)}
.social{left:111px;top:1081px;width:30px;height:30px;border-radius:50%;background:var(--orange)}
.foot-head{font-size:10.5px;font-weight:500;color:var(--white);top:1008px}
.foot-link{font-size:9px;color:var(--white)}
.badge{background:var(--white)}
.foot-rule{left:40px;top:1167px;width:730px;height:1px;background:rgba(255,255,255,.3)}
.copy{left:0;width:810px;top:1178px;text-align:center;font-size:8px;color:var(--white)}
</style>
</head>
<body>

<svg class="backdrop" width="810" height="1200" viewBox="0 0 810 1200" aria-hidden="false">
  <defs>
    <linearGradient id="heroTone" x1="0" y1="0" x2="1" y2="1">
      <stop offset="0" stop-color="#6d6a64"/>
      <stop offset=".5" stop-color="#5a5048"/>
      <stop offset="1" stop-color="#8a6b4c"/>
    </linearGradient>
  </defs>
  <path role="img" aria-label="Photo of a childcare playroom with toys and a play house" d="M0 66 H810 V370 C775 345 748 326 724 318 V350 H86 C55 352 25 360 0 370 Z" fill="url(#heroTone)"/>
  <path d="M0 368 C30 360 60 354 86 350" stroke="var(--green)" stroke-width="2.5" fill="none"/>
  <path d="M724 316 C760 326 790 344 810 364 V372 C788 352 758 334 724 326 Z" fill="var(--green)"/>
  <path role="img" aria-label="Dark photo of a garden behind a fence" d="M0 896 Q405 1010 810 899 V1200 H0 Z" fill="var(--footer)"/>
  <path d="M0 896 Q405 1000 810 899 V912 Q405 1020 0 900 Z" fill="var(--green)"/>
  <ellipse role="img" aria-label="Tree illustration" cx="208" cy="905" rx="30" ry="29" fill="var(--green)"/>
  <ellipse role="img" aria-label="Tree illustration" cx="663" cy="895" rx="56" ry="48" fill="var(--green)"/>
</svg>

<header>
  <div class="abs brand"><span class="dot"></span>Brightfield</div>

  <div class="abs contact" style="left:290px">
    <div class="ic" style="background:var(--blue)">
      <svg width="12" height="14" viewBox="0 0 12 14"><path d="M6 0a5 5 0 0 0-5 5c0 4 5 9 5 9s5-5 5-9a5 5 0 0 0-5-5z" fill="#fff"/><circle cx="6" cy="5" r="1.8" fill="var(--blue)"/></svg>
    </div>
    <div><strong>MAPLEWOOD</strong><span>18 Wattle Grove, Maplewood QLD 4100</span></div>
  </div>

  <div class="abs contact" style="left:479px">
    <div class="ic" style="background:var(--orange)">
      <svg width="13" height="13" viewBox="0 0 24 24"><path d="M6.6 10.8a15 15 0 0 0 6.6 6.6l2.2-2.2a1 1 0 0 1 1-.25 11 11 0 0 0 3.6.6 1 1 0 0 1 1 1V20a1 1 0 0 1-1 1A17 17 0 0 1 3 4a1 1 0 0 1 1-1h3.5a1 1 0 0 1 1 1 11 11 0 0 0 .6 3.6 1 1 0 0 1-.25 1z" fill="#fff"/></svg>
    </div>
    <div><strong>(07) 3000 4521</strong><span>Call Us Now</span></div>
  </div>

  <div class="abs contact" style="left:598px">
    <div class="ic" style="background:var(--green)">
      <svg width="13" height="10" viewBox="0 0 13 10"><rect x=".5" y=".5" width="12" height="9" rx="1" fill="none" stroke="#fff"/><path d="M.5 .8 6.5 6l6-5.2" fill="none" stroke="#fff"/></svg>
    </div>
    <div><strong>maplewood@brightfieldcare.com.au</strong><span>Email Address</span></div>
  </div>

  <nav class="abs nav">
    <a style="left:29px">HOME</a>
    <a style="left:86px">ABOUT US</a>
    <a style="left:162px">PARENT INFO</a>
    <a style="left:254px">OUR PROGRAMS</a>
    <a style="left:361px">TEMPLATE FOR CENTRE</a>
    <a style="left:500px">CONTACT US</a>
    <span class="divider"></span>
    <span class="search">Search.....</span>
    <svg style="position:absolute;left:705px;top:10px" width="11" height="11" viewBox="0 0 11 11"><circle cx="4.5" cy="4.5" r="3.8" fill="none" stroke="#fff" stroke-width="1.1"/><path d="M7.3 7.3 10.3 10.3" stroke="#fff" stroke-width="1.1"/></svg>
  </nav>
</header>

<section>
  <h1 class="abs hero-title">ENROLLMENT</h1>
  <p class="abs hero-copy lead">We'd welcome you to one of our Brightfield Early Learning Centres. If you would like to register your interest in our centres, please fill out the form below. Our educators will contact you to discuss your needs.</p>
  <p class="abs hero-copy note">Please note: filling in this form does not guarantee a place. We recommend visiting a centre for a tour and meeting our friendly educators.</p>
</section>

<main>
  <div class="abs card"></div>
  <h2 class="abs card-title">Enrolment Enquiry</h2>
  <div class="abs card-rule"></div>

  <div class="abs label" style="left:118px;top:317px">Which Centre are you inquiring about?</div>
  <div class="abs field full" style="top:334px">Please select centre
    <span class="toggle"><svg width="9" height="6" viewBox="0 0 9 6"><path d="M.7.7 4.5 4.8 8.3.7" fill="none" stroke="#111" stroke-width="1.2"/></svg></span>
  </div>

  <div class="abs label" style="left:118px;top:369px">Age(s) of your child(ren)?</div>
  <div class="abs label" style="left:409px;top:369px">Date you require care from?</div>
  <div class="abs field left" style="top:386px">Please select centre</div>
  <div class="abs field right" style="top:386px">Date of birth<span class="toggle"></span></div>

  <div class="abs label" style="left:118px;top:421px">Which days are intrested in?</div>
  <div class="abs label" style="left:409px;top:421px">How did you hear about us?</div>
  <div class="abs field left" style="top:438px">Please select<span class="toggle"></span></div>
  <div class="abs field right" style="top:438px">Please select<span class="toggle"></span></div>

  <div class="abs label" style="left:118px;top:472px">Parents first name</div>
  <div class="abs label" style="left:409px;top:472px">Parents last name</div>
  <div class="abs field left" style="top:489px">Enter your first name</div>
  <div class="abs field right" style="top:489px">Enter your last name</div>

  <div class="abs label" style="left:118px;top:525px">Adress</div>
  <div class="abs field full" style="top:541px">Enter your adress</div>

  <div class="abs label" style="left:118px;top:577px">E-mail</div>
  <div class="abs label" style="left:409px;top:577px">Phone</div>
  <div class="abs field left" style="top:595px">Enter your email adress</div>
  <div class="abs field right" style="top:595px">Enter your phone no</div>

  <div class="abs label" style="left:118px;top:630px">Comments</div>
  <div class="abs field full area" style="top:647px">Enter a discription...</div>

  <div class="abs label" style="left:118px;top:721px">Please prove that you are human by solving the equation</div>
  <div class="abs field full" style="top:738px">4+4=?</div>

  <div class="abs submit">SUBMIT</div>
</main>

<footer>
  <div class="abs foot-brand"><span class="dot"></span>Brightfield</div>
  <div class="abs social" role="img" aria-label="Social profile link"></div>

  <div class="abs foot-head" style="left:228px">QUICK LINKS PARENTS</div>
  <div class="abs foot-link" style="left:228px;top:1033px">Our Programs</div>
  <div class="abs foot-link" style="left:228px;top:1052px">Parent</div>
  <div class="abs foot-link" style="left:228px;top:1071px">Information</div>
  <div class="abs foot-link" style="left:228px;top:1091px">About Us</div>
  <div class="abs foot-link" style="left:228px;top:1110px">Contact</div>
  <div class="abs foot-link" style="left:228px;top:1129px">Our Centres</div>

  <div class="abs foot-head" style="left:414px">QUICK LINKS EDUCATORS</div>
  <div class="abs foot-link" style="left:414px;top:1033px">RTO</div>
  <div class="abs foot-link" style="left:414px;top:1057px">Careers</div>
  <div class="abs foot-link" style="left:414px;top:1082px">Our Centres</div>
  <div class="abs foot-link" style="left:414px;top:1106px">About Us</div>
  <div class="abs foot-link" style="left:414px;top:1130px">Our Programs</div>

  <div class="abs badge" role="img" aria-label="Approved program badge" style="left:599px;top:1030px;width:125px;height:32px;border-radius:6px"></div>
  <div class="abs badge" role="img" aria-label="Training certification badge" style="left:599px;top:1091px;width:51px;height:50px"></div>

  <div class="abs foot-rule"></div>
  <div class="abs copy">©&nbsp; Brightfield Early Learning Centre 2024 | Website Design and Development by Northgate Web Hosting by Cloudline Hosting</div>
</footer>

</body>
</html>
```